Business Cards

Hi,
We are due for an update of bussiness cards. I Hvae also included jpg of our current card with old logo just so you can see why we want change). We do have a current logo (attached) however would like the cards to be more modern and edgy, double sided, with the following words (final to be provided in suitable format for printer):
Below are some of the essentials;

FRONT

KRPVN logo
Learn to Dance
Modern Jive and West Coast Swing
0417 862 551

BACK

Dance, it’s cheaper than therapy!
New Dancers – FREE Entry

```html
<!DOCTYPE html>
<html lang="en">
<head>
<meta charset="utf-8">
<title>Kerpvan Dance – Business Cards</title>
<link rel="stylesheet" href="https://fonts.googleapis.com/css2?family=Montserrat:wght@400;500;600;700&display=swap">
<style>
  :root {
    --bg: #4a4a4a;
    --card: #151515;
    --orange: #f7931e;
    --brown: #7a4a12;
    --brown-dark: #5c380d;
    --brown-mid: #8f5614;
    --white: #ffffff;
  }
  * { margin: 0; padding: 0; box-sizing: border-box; }
  html, body {
    width: 1200px; height: 821px; overflow: hidden;
    background: var(--bg);
    font-family: "Montserrat", sans-serif;
  }
  .stage { position: relative; width: 1200px; height: 821px; }
  .card {
    position: absolute; width: 520px; height: 300px;
    background: var(--card); border-radius: 14px; overflow: hidden;
    box-shadow: 0 10px 30px rgba(0,0,0,.35);
  }
  .card-shapes { position: absolute; inset: 0; width: 100%; height: 100%; }
  .card-back { left: 70px; top: 90px; }
  .card-front { left: 610px; top: 420px; }

  .brand-name {
    position: absolute; color: var(--orange);
    font-weight: 500; font-size: 28px; letter-spacing: .5px; white-space: nowrap;
  }
  .card-back .brand-name { left: 0; right: 0; top: 92px; text-align: center; }
  .card-front .brand-name { left: 262px; top: 118px; }

  .back-message {
    position: absolute; left: 0; right: 0; top: 168px;
    text-align: center; color: var(--white); font-size: 13px; line-height: 1.45;
  }
  .accent { color: var(--orange); }

  .front-intro { position: absolute; left: 28px; top: 112px; }
  .front-title { color: var(--orange); font-weight: 700; font-size: 22px; }
  .front-tagline { color: var(--white); font-weight: 500; font-size: 15px; margin-top: 2px; }
  .front-styles { color: var(--orange); font-weight: 600; font-size: 13.5px; margin-top: 20px; }

  .contact-list { position: absolute; left: 300px; top: 198px; list-style: none; }
  .contact-item {
    display: flex; align-items: center; gap: 10px;
    color: var(--white); font-size: 13px; margin-bottom: 8px;
  }
  .contact-icon { width: 13px; height: 13px; flex: none; }
</style>
</head>
<body>
<main class="stage">

  <section class="card card-back" aria-label="Card back">
    <svg class="card-shapes" viewBox="0 0 520 300" aria-hidden="true">
      <polygon points="430,0 520,0 520,58" fill="var(--brown)"/>
      <polygon points="0,212 128,212 0,288" fill="var(--brown)"/>
      <rect x="0" y="287" width="520" height="13" fill="var(--orange)"/>
    </svg>
    <div class="brand-name">Kerpvan Dance</div>
    <p class="back-message">
      <span class="accent">Dance</span>, it’s cheaper than therapy!<br>
      New Dancer - <span class="accent">FREE Entry</span>
    </p>
  </section>

  <section class="card card-front" aria-label="Card front">
    <svg class="card-shapes" viewBox="0 0 520 300" aria-hidden="true">
      <polygon points="350,0 520,0 520,92 452,112" fill="var(--brown-dark)"/>
      <polygon points="452,112 520,92 520,196" fill="var(--brown-mid)"/>
      <polygon points="420,0 520,0 452,112" fill="var(--brown)"/>
      <polygon points="0,238 300,238 262,300 0,300" fill="var(--brown)"/>
    </svg>

    <div class="front-intro">
      <div class="front-title">KRPVN LOGO</div>
      <div class="front-tagline">Learn to Dance</div>
      <div class="front-styles">Modern Jive and West Coast Swing</div>
    </div>

    <div class="brand-name">Kerpvan Dance</div>

    <ul class="contact-list">
      <li class="contact-item">
        <svg class="contact-icon" viewBox="0 0 24 24" aria-hidden="true">
          <path fill="var(--orange)" d="M6.6 10.8a15 15 0 0 0 6.6 6.6l2.2-2.2a1 1 0 0 1 1-.25 11.4 11.4 0 0 0 3.6.57 1 1 0 0 1 1 1V20a1 1 0 0 1-1 1A17 17 0 0 1 3 4a1 1 0 0 1 1-1h3.5a1 1 0 0 1 1 1c0 1.25.2 2.45.57 3.57a1 1 0 0 1-.25 1z"/>
        </svg>
        0417 862 551
      </li>
      <li class="contact-item">
        <svg class="contact-icon" viewBox="0 0 24 24" aria-hidden="true">
          <circle cx="12" cy="12" r="9" fill="none" stroke="var(--orange)" stroke-width="2.4"/>
          <path d="M3 12h18M12 3c3 3 3 15 0 18M12 3c-3 3-3 15 0 18" fill="none" stroke="var(--orange)" stroke-width="1.8"/>
        </svg>
        www.kerpvandance.com.au
      </li>
    </ul>
  </section>

</main>
</body>
</html>
```